Brightway Inc. Business Card Design

Brightway Inc. is in search of a great clean design for our business cards!

Looking to incorporate our full logo and watermark on side one (however, I am open to having the text and watermark separated within the design.)

On side two, I am looking to have contact information (Name, Position, Phone #, Email, Website (www.thebrightway.ca). Can have the logo and/or watermark as part of the design if applicable.

Please add tagline "Where Shine Counts" on either side 1 or 2. This tagline can be in a sans serif, serif or cursive font as long as it compliments overall design. Capitalization can be title or sentence case depending on how it fits within the design.

Get creative!! Looking for a clean, crisp, premium design! Looking for a glossy card finish with spot UV features when printed. Cards will also be printed with rounded corners. Standard dimensions (3.5 x 2).

Target Market(s)

B2B - primary clients are business owners or property management corporations. (residential jobs are few and far between)

Industry/Entity Type

Business

Contact Information for Business Card

- clean, crisp design
- double sided
- spot UV accents and glossy finish upon printing
- standard business card size (3.5 x 2) with rounded corners
- please see project description for requirements per side

Font styles to use
Sans Serif

Requirements
Must have
• - adequate bleeds with print ready files
• - cohesive design elements between side 1 & 2
• - spot UV elements (can be on both sides or just one, use your discretion)
• - colour pallet should match the logo file provided
• - incorporate tagline "where shine counts" (this tagline can be in a serif or sans serif font as long as it is complimentary to the overall design.
Nice to have
• - Premium elements with a clean design
Should not have
• - Please omit cartoon or whimsical like designs, think premium.
• - Colours should not stray from the pallet of the provided logo.

```html
<!DOCTYPE html>
<html lang="en">
<head>
<meta charset="utf-8">
<title>Brightway Inc. Business Cards</title>
<link href="https://fonts.googleapis.com/css2?family=Montserrat:wght@400;500;700;800&display=swap" rel="stylesheet">
<style>
  :root {
    --bg: #1b1b1b;
    --white: #ffffff;
    --teal: #12b8bd;
    --navy: #1b2656;
    --ink: #2e2e3a;
    --muted: #4a4a55;
  }
  * { margin: 0; padding: 0; box-sizing: border-box; }
  html, body { width: 1200px; height: 1200px; overflow: hidden; background: var(--bg); }
  body { font-family: "Montserrat", Arial, sans-serif; position: relative; }

  .card {
    position: absolute;
    left: 250px;
    width: 700px;
    height: 400px;
    border-radius: 36px;
    overflow: hidden;
  }
  .card--front { top: 150px; background: var(--white); }
  .card--back { top: 650px; background: var(--teal); display: flex; align-items: center; justify-content: center; }

  .brand {
    display: flex; align-items: center; gap: 14px;
    font-weight: 800; letter-spacing: 0.5px; white-space: nowrap;
  }
  .brand__mark { width: 32px; height: 32px; flex: none; }
  .brand--front {
    position: absolute; top: 82px; left: 0; right: 0;
    justify-content: center; color: var(--navy); font-size: 44px;
  }
  .brand--front .brand__mark { background: var(--teal); }
  .brand--back { color: var(--white); font-size: 54px; }
  .brand--back .brand__mark { background: var(--white); width: 40px; height: 40px; }

  .person { position: absolute; left: 48px; top: 160px; }
  .person__name { font-size: 30px; font-weight: 700; line-height: 1; white-space: nowrap; }
  .person__first { color: var(--teal); }
  .person__last { color: var(--navy); }
  .person__role { font-size: 16px; color: var(--muted); margin-top: 8px; }

  .divider { position: absolute; left: 40px; right: 40px; top: 226px; height: 1px; background: var(--navy); }

  .contacts { position: absolute; left: 48px; top: 240px; list-style: none; }
  .contacts li { display: flex; align-items: center; gap: 10px; font-size: 17px; color: var(--ink); height: 26px; white-space: nowrap; }
  .contacts svg { width: 14px; height: 14px; fill: var(--navy); flex: none; }

  .tagline { position: absolute; right: 46px; top: 286px; font-size: 17px; color: var(--ink); letter-spacing: 1px; white-space: nowrap; }

  .bands { position: absolute; left: 0; bottom: 0; width: 700px; height: 40px; }
</style>
</head>
<body>

<section class="card card--front" aria-label="Card front">
  <div class="brand brand--front"><span class="brand__mark"></span>Brightway Inc.</div>

  <div class="person">
    <div class="person__name"><span class="person__first">DANA</span> <span class="person__last">WHITLOCK</span></div>
    <div class="person__role">Director</div>
  </div>

  <div class="divider"></div>

  <ul class="contacts">
    <li><svg viewBox="0 0 24 24"><path d="M6.6 10.8a15 15 0 0 0 6.6 6.6l2.2-2.2c.3-.3.7-.4 1-.2 1.1.4 2.3.6 3.6.6.6 0 1 .4 1 1V20c0 .6-.4 1-1 1A17 17 0 0 1 3 4c0-.6.4-1 1-1h3.5c.6 0 1 .4 1 1 0 1.3.2 2.5.6 3.6.1.3 0 .7-.2 1z"/></svg>555-014-2290</li>
    <li><svg viewBox="0 0 24 24"><path d="M12 2a10 10 0 1 0 0 20 10 10 0 0 0 0-20zm6.9 6h-3a15 15 0 0 0-1.3-3.9A8 8 0 0 1 18.9 8zM12 4c.8 1.2 1.5 2.5 1.9 4h-3.8c.4-1.5 1.1-2.8 1.9-4zM4.3 14a8 8 0 0 1 0-4h3.4a16 16 0 0 0 0 4zm.8 2h3a15 15 0 0 0 1.3 3.9A8 8 0 0 1 5.1 16zm3-8h-3a8 8 0 0 1 4.3-3.9A15 15 0 0 0 8.1 8zM12 20c-.8-1.2-1.5-2.5-1.9-4h3.8c-.4 1.5-1.1 2.8-1.9 4zm2.3-6H9.7a14 14 0 0 1 0-4h4.6a14 14 0 0 1 0 4zm.3 5.9A15 15 0 0 0 15.9 16h3a8 8 0 0 1-4.3 3.9zM16.3 14a16 16 0 0 0 0-4h3.4a8 8 0 0 1 0 4z"/></svg>www.thebrightway.ca</li>
    <li><svg viewBox="0 0 24 24"><rect x="2" y="5" width="20" height="14" rx="2"/></svg>info@thebrightway.ca</li>
  </ul>

  <div class="tagline">Where Shine Counts</div>

  <svg class="bands" viewBox="0 0 700 40" preserveAspectRatio="none" aria-hidden="true">
    <polygon points="0,18 455,18 445,40 0,40" fill="var(--teal)"/>
    <polygon points="466,0 700,0 700,40 452,40" fill="var(--navy)"/>
  </svg>
</section>

<section class="card card--back" aria-label="Card back">
  <div class="brand brand--back"><span class="brand__mark"></span>Brightway Inc.</div>
</section>

</body>
</html>
```